Powerpoint master slide deck for power point presentation by members of my company

To design a master slide deck for powerpoint presentation for a Orthopaedic Clinic Based in Singapore

```html
<!DOCTYPE html>
<html lang="en">
<head>
<meta charset="UTF-8">
<title>Stride Joint Clinic – Master Slide Deck</title>
<link href="https://fonts.googleapis.com/css2?family=Michroma&family=Open+Sans:wght@400;600;700&display=swap" rel="stylesheet">
<style>
  :root{
    --page:#0c1a1d;
    --slide:#10272b;
    --slide-deep:#0d2124;
    --teal:#45b8a6;
    --teal-soft:#3a9d8f;
    --teal-dark:#1d5e57;
    --ink:#0b1d20;
    --white:#ffffff;
    --muted:#a9c2c0;
    --card:#f2f5f5;
  }
  *{box-sizing:border-box;margin:0;padding:0}
  html,body{width:1200px;height:4024px;overflow:hidden}
  body{background:var(--page);font-family:"Open Sans",Arial,sans-serif;color:var(--white);position:relative}
  .slide{position:absolute;left:40px;width:1120px;height:600px;background:var(--slide);overflow:hidden}
  .slide::after{content:"";position:absolute;left:50px;right:50px;bottom:22px;height:2px;background:var(--teal)}
  .slide.cover::after{display:none}
  .slide-title{position:absolute;left:50px;top:44px;font-family:"Michroma",sans-serif;font-size:26px;letter-spacing:2px;text-transform:uppercase;color:var(--white)}
  .slide-title span{color:var(--teal)}
  .brand{position:absolute;right:50px;top:38px;display:flex;align-items:center;gap:10px}
  .brand-mark{width:30px;height:30px;background:var(--teal);border-radius:4px}
  .brand-name{font-family:"Open Sans",sans-serif;font-weight:700;font-size:16px;letter-spacing:1px;color:var(--white);text-transform:uppercase}

  /* Cover */
  .cover{background:var(--slide-deep)}
  .cover .brand{left:50px;right:auto;top:60px;gap:14px}
  .cover .brand-mark{width:46px;height:46px}
  .cover .brand-name{font-size:30px}
  .cover-eyebrow{position:absolute;left:50px;top:150px;font-weight:700;font-size:15px}
  .cover-title{position:absolute;left:50px;top:180px;width:560px;font-family:"Michroma",sans-serif;font-size:31px;line-height:1.35;text-transform:uppercase}
  .cover-lead{position:absolute;left:50px;top:282px;width:520px;font-size:13px;color:var(--muted);line-height:1.5}
  .socials{position:absolute;left:50px;top:330px;display:flex;gap:10px}
  .socials i{width:22px;height:22px;border-radius:50%;background:var(--teal)}
  .cover-art{position:absolute;left:640px;top:120px;width:440px;height:440px;border-radius:40px 40px 0 40px;background:linear-gradient(140deg,#4fc2b0,#2c8679)}

  /* Services */
  .services{position:absolute;left:50px;top:130px;width:1020px;display:grid;grid-template-columns:1fr 1fr;column-gap:40px;row-gap:26px}
  .service{position:relative;height:58px;border-radius:29px;background:var(--teal-soft);color:var(--ink);display:flex;flex-direction:column;justify-content:center}
  .service.left{padding:0 84px 0 24px;text-align:right}
  .service.right{padding:0 24px 0 84px;text-align:left}
  .service h3{font-size:14px;font-weight:700}
  .service p{font-size:9.5px;line-height:1.3}
  .service .icon{position:absolute;top:3px;width:52px;height:52px;border-radius:50%;background:var(--slide);border:3px solid var(--teal);display:flex;align-items:center;justify-content:center}
  .service.left .icon{right:4px}
  .service.right .icon{left:4px}

  /* Benefits */
  .benefit-photo{position:absolute;left:220px;top:120px;width:370px;height:330px;background:linear-gradient(135deg,#5b8aa0,#2f4d5a 60%,#1f3540)}
  .benefits{position:absolute;left:630px;top:170px;width:440px;list-style:none}
  .benefits li{position:relative;padding-left:22px;font-size:12.5px;font-weight:600;line-height:1.5;margin-bottom:18px}
  .benefits li::before{content:"";position:absolute;left:0;top:6px;width:9px;height:9px;border-radius:50%;background:var(--teal)}

  /* Team */
  .member{position:absolute;top:110px;width:300px}
  .member .portrait{width:300px;height:230px;background:linear-gradient(160deg,#1f3f45,#0f2428)}
  .member h3{margin-top:16px;font-size:14px;font-weight:700}
  .member .role{font-size:11px;color:var(--muted);margin-bottom:10px}
  .member p{font-size:9.5px;line-height:1.5;color:var(--muted);margin-bottom:6px}

  /* FAQ */
  .faq{position:absolute;left:120px;top:150px;width:880px;display:grid;grid-template-columns:1fr 1fr;column-gap:40px;row-gap:24px}
  .faq-item{height:46px;background:var(--card);color:var(--ink);border-radius:4px;display:flex;align-items:center;justify-content:space-between;padding:0 10px 0 16px;font-size:11.5px;font-weight:600}
  .faq-item .chev{width:26px;height:26px;border-radius:50%;background:var(--teal);display:flex;align-items:center;justify-content:center;flex:none}

  /* Articles */
  .articles{position:absolute;left:60px;top:130px;width:1000px;display:grid;grid-template-columns:repeat(3,1fr);gap:30px}
  .article .thumb{position:relative;height:200px}
  .article .tag{position:absolute;right:10px;top:10px;background:var(--teal);color:var(--ink);font-size:9px;font-weight:700;padding:3px 8px;border-radius:3px}
  .article h3{margin-top:14px;font-size:14px;font-weight:700;line-height:1.35}
  .article .date{margin:8px 0;font-size:10px;color:var(--muted);display:flex;align-items:center;gap:6px}
  .article .date::before{content:"";width:8px;height:8px;border-radius:50%;background:var(--teal)}
  .article p{font-size:9.5px;line-height:1.5;color:var(--muted)}
</style>
</head>
<body>

<!-- Cover -->
<section class="slide cover" style="top:60px">
  <div class="brand"><div class="brand-mark"></div><div class="brand-name">Stride Joint Clinic</div></div>
  <p class="cover-eyebrow">Double Fellowship Trained Orthopaedic Surgeons</p>
  <h1 class="cover-title">Singapore's Hip &amp; Knee Specialist</h1>
  <p class="cover-lead">Our mission is to promote individualised care that meets the needs and goals of every patient</p>
  <div class="socials"><i></i><i></i></div>
  <div class="cover-art" role="img" aria-label="Illustration of a knee joint in profile"></div>
</section>

<!-- Services -->
<section class="slide" style="top:720px">
  <h2 class="slide-title">What <span>We Do</span></h2>
  <div class="brand"><div class="brand-mark"></div><div class="brand-name">Stride Joint Clinic</div></div>
  <div class="services">
    <div class="service left"><h3>Hip Evaluation</h3><p>Thorough assessment of hip pain, stiffness and mobility to guide the right treatment plan.</p><div class="icon"></div></div>
    <div class="service right"><h3>Knee Evaluation</h3><p>Detailed review of knee function, alignment and imaging to pinpoint the cause of pain.</p><div class="icon"></div></div>
    <div class="service left"><h3>Cartilage Repair</h3><p>Modern techniques that restore damaged cartilage and help protect the joint long term.</p><div class="icon"></div></div>
    <div class="service right"><h3>Meniscus Repair</h3><p>Keyhole repair of torn meniscus to preserve knee cushioning and return to activity.</p><div class="icon"></div></div>
    <div class="service left"><h3>Knee Replacement</h3><p>Partial and total knee replacement to relieve arthritis pain and restore movement.</p><div class="icon"></div></div>
    <div class="service right"><h3>ACL Tear and Reconstruction</h3><p>Ligament reconstruction for athletes and active patients seeking a stable knee again.</p><div class="icon"></div></div>
    <div class="service left"><h3>Bone Wellness</h3><p>Screening and care for bone density, strength and healthy ageing of the skeleton.</p><div class="icon"></div></div>
    <div class="service right"><h3>Hip Replacement</h3><p>Precise hip replacement surgery designed for faster recovery and lasting comfort.</p><div class="icon"></div></div>
  </div>
</section>

<!-- Benefits -->
<section class="slide" style="top:1380px">
  <h2 class="slide-title">Key <span>Benefits</span></h2>
  <div class="brand"><div class="brand-mark"></div><div class="brand-name">Stride Joint Clinic</div></div>
  <div class="benefit-photo" role="img" aria-label="Photo of surgeons operating in a theatre"></div>
  <ul class="benefits">
    <li>Our initial consultation begins at $140.00 (w. GST).</li>
    <li>We collaborate with many insurance providers, including corporate, which ensure seamless and potentially cashless visits to the clinic.</li>
    <li>Our clinic is on the panel of most Integrated Shield Plans, Singapore.</li>
    <li>We adhere to National Health Authority fee benchmarks.</li>
  </ul>
</section>

<!-- Team -->
<section class="slide" style="top:2040px">
  <h2 class="slide-title">Our <span>Team</span></h2>
  <div class="brand"><div class="brand-mark"></div><div class="brand-name">Stride Joint Clinic</div></div>
  <div class="member" style="left:220px">
    <div class="portrait" role="img" aria-label="Portrait photo of Dr. Marcus Teo"></div>
    <h3>Dr. Marcus Teo</h3>
    <p class="role">Orthopaedic Surgery Specialist</p>
    <p>Dr. Teo is an orthopaedic surgeon with a special interest in hip and knee surgery, sports injuries and joint preservation.</p>
    <p>He completed fellowship training abroad in arthroplasty and sports surgery, and now leads the clinic's knee programme.</p>
    <p>He is a visiting consultant at a major general hospital.</p>
  </div>
  <div class="member" style="left:620px">
    <div class="portrait" role="img" aria-label="Portrait photo of Dr. Lim Wei Ling"></div>
    <h3>Dr. Lim Wei Ling</h3>
    <p class="role">Orthopaedic Surgery Specialist</p>
    <p>Dr. Lim is an orthopaedic surgeon focused on hip and knee care, with a keen interest in minimally invasive joint replacement.</p>
    <p>She trained in two overseas fellowships covering complex revision surgery, cartilage repair and ligament reconstruction for active patients.</p>
  </div>
</section>

<!-- FAQ -->
<section class="slide" style="top:2700px">
  <h2 class="slide-title">Frequently Asked <span>Questions</span></h2>
  <div class="brand"><div class="brand-mark"></div><div class="brand-name">Stride Joint Clinic</div></div>
  <div class="faq">
    <div class="faq-item">How Will the doctor assess my condition ?<span class="chev"><svg width="10" height="10" viewBox="0 0 10 10"><path d="M2 3.5 5 6.5 8 3.5" fill="none" stroke="#0b1d20" stroke-width="1.6"/></svg></span></div>
    <div class="faq-item">Will my medical treatment be covered by insurance ?<span class="chev"><svg width="10" height="10" viewBox="0 0 10 10"><path d="M2 3.5 5 6.5 8 3.5" fill="none" stroke="#0b1d20" stroke-width="1.6"/></svg></span></div>
    <div class="faq-item">Will the consultation &amp; treatment be claimable CareSave ?<span class="chev"><svg width="10" height="10" viewBox="0 0 10 10"><path d="M2 3.5 5 6.5 8 3.5" fill="none" stroke="#0b1d20" stroke-width="1.6"/></svg></span></div>
    <div class="faq-item">If I have Persistent knee pain, I would need surgery ?<span class="chev"><svg width="10" height="10" viewBox="0 0 10 10"><path d="M2 3.5 5 6.5 8 3.5" fill="none" stroke="#0b1d20" stroke-width="1.6"/></svg></span></div>
    <div class="faq-item">Will there be any treatment done in the clinic ?<span class="chev"><svg width="10" height="10" viewBox="0 0 10 10"><path d="M2 3.5 5 6.5 8 3.5" fill="none" stroke="#0b1d20" stroke-width="1.6"/></svg></span></div>
    <div class="faq-item">Can Xrays or MRIs be done on the same day as the consultation ?<span class="chev"><svg width="10" height="10" viewBox="0 0 10 10"><path d="M2 3.5 5 6.5 8 3.5" fill="none" stroke="#0b1d20" stroke-width="1.6"/></svg></span></div>
    <div class="faq-item">Are the doctors good with sports injuries ?<span class="chev"><svg width="10" height="10" viewBox="0 0 10 10"><path d="M2 3.5 5 6.5 8 3.5" fill="none" stroke="#0b1d20" stroke-width="1.6"/></svg></span></div>
    <div class="faq-item">Does the clinic see conditions other than Hip &amp; Knee Conditions ?<span class="chev"><svg width="10" height="10" viewBox="0 0 10 10"><path d="M2 3.5 5 6.5 8 3.5" fill="none" stroke="#0b1d20" stroke-width="1.6"/></svg></span></div>
  </div>
</section>

<!-- Articles -->
<section class="slide" style="top:3360px">
  <h2 class="slide-title">Latest <span>Articles</span></h2>
  <div class="brand"><div class="brand-mark"></div><div class="brand-name">Stride Joint Clinic</div></div>
  <div class="articles">
    <article class="article">
      <div class="thumb" role="img" aria-label="Photo of a person lifting weights at the gym" style="background:linear-gradient(135deg,#2c4a55,#15262c)"><span class="tag">Fitness</span></div>
      <h3>How to protect our back during strength training at the gym</h3>
      <div class="date">April 7, 2023</div>
      <p>Lifting with good form keeps the spine safe. We share simple tips on posture, bracing and load choice so your workouts stay strong and pain free.</p>
    </article>
    <article class="article">
      <div class="thumb" role="img" aria-label="Photo of feet walking on a grassy path" style="background:linear-gradient(135deg,#5f8a4a,#2d4a2a)"><span class="tag">Wellness</span></div>
      <h3>The Health Benefits of Walking</h3>
      <div class="date">May 1, 2023</div>
      <p>A daily walk supports joint health, heart fitness and mood. Learn how far to go, what to wear and how to build the habit at any age.</p>
    </article>
    <article class="article">
      <div class="thumb" role="img" aria-label="Photo of a swimmer in a blue pool" style="background:linear-gradient(135deg,#4aa6c9,#1d5c7a)"><span class="tag">Recovery</span></div>
      <h3>How Swimming Can Help With Injury Recovery</h3>
      <div class="date">May 1, 2023</div>
      <p>Water takes weight off sore joints while keeping muscles working. Discover why swimming is a gentle, effective part of many rehab plans.</p>
    </article>
  </div>
</section>

</body>
</html>
```